Dozing Heron

Need a business card for our restaurant. Restaurant and Bar in the mountains of North Idaho. Rustic looking card

Contact Information for Business Card

rustic design, wood and metal looking, primarily neutral colors

Requirements
Must have
• Name, address, phone number, website, email address

```html
<!DOCTYPE html>
<html lang="en">
<head>
<meta charset="utf-8">
<title>Dozing Heron – Business Card</title>
<link href="https://fonts.googleapis.com/css2?family=Montserrat:wght@400;500;700&display=swap" rel="stylesheet">
<style>
  :root {
    --backdrop: #2a2a2a;
    --card-top: #1d1d1d;
    --card-bottom: #0e0e0e;
    --ink: #f4f4f4;
    --ink-soft: #d8d8d8;
  }
  * { margin: 0; padding: 0; box-sizing: border-box; }
  html, body { width: 1200px; height: 874px; overflow: hidden; }
  body {
    background: var(--backdrop);
    font-family: "Montserrat", sans-serif;
    color: var(--ink);
    display: flex;
    flex-direction: column;
    align-items: center;
    justify-content: center;
    gap: 34px;
  }
  .card {
    width: 690px;
    height: 394px;
    border-radius: 22px;
    background: linear-gradient(160deg, var(--card-top), var(--card-bottom));
    box-shadow: 0 12px 30px rgba(0,0,0,.45);
    position: relative;
  }
  .brand {
    display: flex;
    flex-direction: column;
    align-items: center;
    justify-content: center;
    gap: 14px;
  }
  .brand-ring {
    border: 4px solid var(--ink);
    border-radius: 50%;
  }
  .brand-name {
    font-weight: 500;
    letter-spacing: .14em;
    text-transform: uppercase;
    color: var(--ink);
    text-align: center;
  }
  .card-front { display: flex; align-items: center; justify-content: center; }
  .card-front .brand-ring { width: 150px; height: 150px; }
  .card-front .brand-name { font-size: 26px; }

  .card-back .brand { position: absolute; left: 42px; top: 34px; gap: 10px; }
  .card-back .brand-ring { width: 96px; height: 96px; border-width: 3px; }
  .card-back .brand-name { font-size: 15px; }

  .contact {
    position: absolute;
    left: 48px;
    bottom: 42px;
    font-size: 18px;
    line-height: 1.35;
    color: var(--ink-soft);
  }
  .contact-address { margin-bottom: 20px; }
  .contact-line { display: flex; align-items: center; gap: 10px; }
  .contact-line svg { width: 15px; height: 15px; fill: var(--ink-soft); flex: none; }

  .person {
    position: absolute;
    right: 60px;
    bottom: 92px;
    text-align: right;
  }
  .person-name { font-size: 30px; font-weight: 700; color: var(--ink); }
  .person-title { font-size: 18px; color: var(--ink-soft); margin-top: 2px; }
</style>
</head>
<body>
  <section class="card card-front">
    <div class="brand">
      <div class="brand-ring"></div>
      <div class="brand-name">The Dozing Heron</div>
    </div>
  </section>

  <section class="card card-back">
    <div class="brand">
      <div class="brand-ring"></div>
      <div class="brand-name">The Dozing Heron</div>
    </div>

    <div class="contact">
      <p class="contact-address">Your address, City<br>State, Zip 1234</p>
      <p class="contact-line">
        <svg viewBox="0 0 16 16" aria-hidden="true"><path d="M3 1h3l1.5 4-2 1.2a9 9 0 0 0 4.3 4.3L11 8.5l4 1.5v3a2 2 0 0 1-2 2A12 12 0 0 1 1 3a2 2 0 0 1 2-2z"/></svg>
        123 456 789
      </p>
      <p class="contact-line">
        <svg viewBox="0 0 16 16" aria-hidden="true"><path d="M1 3h14v10H1z M2 4l6 5 6-5v-.2H2z" fill-rule="evenodd"/></svg>
        info@yourmail.com
      </p>
      <p class="contact-line">
        <svg viewBox="0 0 16 16" aria-hidden="true"><path d="M8 1a7 7 0 1 0 0 14A7 7 0 0 0 8 1zm0 1.5c.9 1 1.5 2.6 1.7 4.5H6.3C6.5 5.1 7.1 3.5 8 2.5zM2.6 9h2.2c.1 1.6.5 3 1.1 4A5.5 5.5 0 0 1 2.6 9zm0-2a5.5 5.5 0 0 1 3.3-4c-.6 1-1 2.4-1.1 4zm5.4 6.5c-.9-1-1.5-2.6-1.7-4.5h3.4c-.2 1.9-.8 3.5-1.7 4.5zm2.1-.5c.6-1 1-2.4 1.1-4h2.2a5.5 5.5 0 0 1-3.3 4zm1.1-6c-.1-1.6-.5-3-1.1-4a5.5 5.5 0 0 1 3.3 4z"/></svg>
        www.yourwebsite.com
      </p>
    </div>

    <div class="person">
      <p class="person-name">Owen Hartley</p>
      <p class="person-title">Managing Director</p>
    </div>
  </section>
</body>
</html>
```